Sign Advertisment for Condominium Development

I need a sign created that will be placed in front of a building that is being converted into a luxury condominium development.

The sign needs to say:

Two, Boutique Luxury Condominiums Delivering late 2015.

Luxury Finishes // Designer Kitchens and Bath // Each Unit over 2,000 Square Feet

Deeded Parking Included with Each Unit

To Learn More, Contact:

Marissa Talbot or Vernon Pike
(202) 555-0147
Marissa.Talbot@example-realty.com

I need a small disclaimer at the bottom stating:

These Condominium(s) have not been registered by the Office of Residential Standards and Property Oversight Bureau Tenancy Transition and Transfer Section. A Condominium Unit may be reserved on a non-binding reservation agreement, but no contract of sale or lease that is binding on the purchaser may be entered into prior to registration.

Target Market(s)

Young professionals seeking luxury condominium

Industry/Entity Type

Building

Font styles to use
Serif

Colors
00a88f
ffffff

```html
<!DOCTYPE html>
<html lang="en">
<head>
<meta charset="utf-8">
<title>Two Boutique Luxury Condominiums – Sign</title>
<link rel="stylesheet" href="https://fonts.googleapis.com/css2?family=Montserrat:wght@600;800&family=Kanit:wght@300&display=swap">
<style>
  :root {
    --teal: #00a88f;
    --white: #ffffff;
    --ink: #231f20;
    --bar-grey: #a7a9ac;
    --backdrop: #000000;
  }
  * { margin: 0; padding: 0; box-sizing: border-box; }
  html, body {
    width: 1200px; height: 835px; overflow: hidden;
    background: var(--backdrop);
  }
  .sign {
    position: absolute; left: 79px; top: 71px;
    width: 1042px; height: 694px;
    background: var(--white);
    color: var(--ink);
    overflow: hidden;
  }
  .sign > * { position: absolute; white-space: nowrap; line-height: 1; }

  .header-band {
    left: 0; top: 0; width: 1042px; height: 250px;
    background: var(--teal);
  }
  .title-main, .title-sub, .delivery { left: 0; width: 1042px; text-align: center; }
  .title-main {
    top: 32px; font: 800 92px "Montserrat", sans-serif; color: var(--white);
  }
  .title-sub {
    top: 118px; font: 800 60px "Montserrat", sans-serif; color: var(--white);
  }
  .delivery {
    top: 187px; font: 300 40px "Kanit", sans-serif; color: var(--ink);
  }

  .interior-render {
    left: 470px; top: 250px; width: 572px; height: 444px;
    background:
      radial-gradient(ellipse 120px 70px at 300px 240px, rgba(230, 80, 70, 0.35), transparent),
      linear-gradient(90deg, rgba(255,255,255,1) 0%, rgba(236,236,236,0.9) 40%, #e4e4e4 100%);
  }

  .feature { left: 64px; font: 300 33px "Kanit", sans-serif; color: var(--ink); }
  .feature::before {
    content: ""; position: absolute; left: -22px; top: 8px;
    width: 11px; height: 23px; background: var(--bar-grey);
  }
  .feature-rule { left: 0; height: 2px; background: var(--teal); }

  .contact-label { left: 46px; top: 563px; font: 600 22px "Montserrat", sans-serif; }
  .contact-names { left: 44px; top: 598px; font: 600 35px "Montserrat", sans-serif; color: var(--teal); }
  .contact-phone { left: 636px; top: 560px; font: 600 44px "Montserrat", sans-serif; }
  .contact-email { left: 637px; top: 614px; font: 300 23px "Kanit", sans-serif; }

  .disclaimer {
    left: 0; top: 652px; width: 1042px; text-align: center;
    font: 300 11px "Kanit", sans-serif; line-height: 15px;
  }
</style>
</head>
<body>
  <main class="sign">
    <div class="header-band"></div>
    <h1 class="title-main">TWO BOUTIQUE</h1>
    <h2 class="title-sub">LUXURY CONDOMINIUMS</h2>
    <p class="delivery">Delivering late 2015.</p>

    <div class="interior-render" role="img" aria-label="Architectural sketch blending into a rendered modern living room with shelving, red sofa and large screen"></div>

    <p class="feature" style="top:293px">Luxury Finishes</p>
    <div class="feature-rule" style="top:336px; width:521px"></div>
    <p class="feature" style="top:347px">Designer Kitchens and Bath</p>
    <div class="feature-rule" style="top:389px; width:521px"></div>
    <p class="feature" style="top:400px">Each Unit over 2,000 Sq.Ft.</p>
    <div class="feature-rule" style="top:443px; width:506px"></div>
    <p class="feature" style="top:454px; line-height:40px; margin-top:-6px">Deeded Parking Included<br>with Each Unit</p>
    <div class="feature-rule" style="top:533px; width:301px"></div>

    <p class="contact-label">To Learn More, Contact:</p>
    <p class="contact-names">Marissa Talbot or Vernon Pike</p>
    <p class="contact-phone">(202) 555-0147</p>
    <p class="contact-email">Marissa.Talbot@example-realty.com</p>

    <p class="disclaimer">These Condominium(s) have not been registered by the Office of Residential Standards and Property Oversight Bureau Tenancy Transition and Transfer Section.<br>A Condominium Unit may be reserved on a non-binding reservation agreement, but no contract of sale or lease that is binding on the purchaser may be entered into prior to registration.</p>
  </main>
</body>
</html>
```